Veltrona Services

Double sided business cards with color on front and black and white on back. I have basic ideas and graphics, but am looking for someone to take them to the next level

```html
<!DOCTYPE html>
<html lang="en">
<head>
<meta charset="utf-8">
<title>Veltrona Services – Business Cards</title>
<link rel="stylesheet" href="https://fonts.googleapis.com/css2?family=Barlow+Semi+Condensed:wght@400;500&family=Krona+One&display=swap">
<style>
  :root {
    --backdrop: #262626;
    --card-black: #050505;
    --panel-white: #f7f7f7;
    --panel-shade: #e4e4e4;
    --brand-blue: #4a86a8;
    --ink: #111111;
    --accent-red: #d8323a;
    --accent-green: #5cc23a;
    --accent-yellow: #e3c82a;
    --band-light: #f2f2f2;
    --band-dark: #cfcfcf;
    --mark-grey: #d6d6d6;
  }
  * { margin: 0; padding: 0; box-sizing: border-box; }
  html, body {
    width: 1200px;
    height: 732px;
    overflow: hidden;
    background: var(--backdrop);
  }
  .canvas {
    position: relative;
    width: 1200px;
    height: 732px;
  }
  .card {
    position: absolute;
    top: 242px;
    width: 436px;
    height: 248px;
    box-shadow: 0 6px 18px rgba(0,0,0,0.55);
  }
  .card--front { left: 144px; }
  .card--back  { left: 621px; }
  .card svg { display: block; width: 100%; height: 100%; }

  .brand-name {
    font-family: "Barlow Semi Condensed", sans-serif;
    font-weight: 500;
    font-size: 27px;
    fill: var(--brand-blue);
  }
  .phone {
    font-family: "Barlow Semi Condensed", sans-serif;
    font-weight: 400;
    font-size: 24px;
    fill: var(--ink);
  }
  .tagline {
    font-family: "Krona One", sans-serif;
    font-size: 13.5px;
    fill: var(--ink);
    letter-spacing: 0.4px;
  }
  .back-name {
    font-family: "Krona One", sans-serif;
    font-size: 14px;
    fill: var(--panel-white);
    letter-spacing: 1px;
  }
</style>
</head>
<body>
<main class="canvas">

  <!-- Front of card -->
  <section class="card card--front" aria-label="Business card front">
    <svg viewBox="0 0 436 248" xmlns="http://www.w3.org/2000/svg">
      <defs>
        <linearGradient id="panelGradient" x1="0" y1="1" x2="1" y2="0">
          <stop offset="0" stop-color="var(--panel-shade)"/>
          <stop offset="0.5" stop-color="var(--panel-white)"/>
          <stop offset="1" stop-color="#ffffff"/>
        </linearGradient>
      </defs>
      <rect class="card-base" width="436" height="248" fill="var(--card-black)"/>
      <polygon class="white-panel" points="314,0 436,0 436,209 416,228 85,228" fill="url(#panelGradient)"/>
      <polygon class="panel-facet" points="233,111 117,228 160,228 262,111" fill="#e9e9e9" opacity="0.7"/>
      <polygon class="panel-facet" points="250,150 174,228 250,228 300,150" fill="#ebebeb" opacity="0.6"/>
      <line class="accent-line accent-line--red" x1="300" y1="0" x2="138" y2="165" stroke="var(--accent-red)" stroke-width="1.2"/>
      <line class="accent-line accent-line--green" x1="76" y1="239" x2="291" y2="239" stroke="var(--accent-green)" stroke-width="1.2"/>
      <line class="accent-line accent-line--yellow" x1="423" y1="237" x2="435" y2="225" stroke="var(--accent-yellow)" stroke-width="1.2"/>
      <circle class="brand-circle" cx="344" cy="87" r="66" fill="none" stroke="var(--mark-grey)" stroke-width="3"/>
      <text class="brand-name" x="412" y="190" text-anchor="end">VELTRONA SERVICES</text>
      <text class="phone" x="412" y="215" text-anchor="end">555-210-4837</text>
    </svg>
  </section>

  <!-- Back of card -->
  <section class="card card--back" aria-label="Business card back">
    <svg viewBox="0 0 436 248" xmlns="http://www.w3.org/2000/svg">
      <defs>
        <linearGradient id="bandGradient" x1="0" y1="0" x2="1" y2="0">
          <stop offset="0" stop-color="var(--band-light)"/>
          <stop offset="1" stop-color="var(--band-dark)"/>
        </linearGradient>
      </defs>
      <rect class="card-base" width="436" height="248" fill="var(--card-black)"/>
      <circle class="brand-circle" cx="218" cy="72" r="42" fill="var(--panel-white)"/>
      <text class="back-name" x="218" y="146" text-anchor="middle">VELTRONA SERVICES</text>
      <rect class="tagline-band" x="0" y="181" width="436" height="67" fill="url(#bandGradient)"/>
      <text class="tagline" x="218" y="211" text-anchor="middle">A CURATED EXPERIENCE</text>
      <text class="tagline" x="218" y="232" text-anchor="middle">ALL THAT IS PROMISED IS CLARITY</text>
    </svg>
  </section>

</main>
</body>
</html>
```